#1 Selling Sweden weight loss supplement comes to USA - LABEL needed!

The number one weight loss in Sweden is coming to USA

-I need a label that is clean and simple but somehow represents, in an abstract way, weight loss or slender.
-The product and water mixed is all the is needed. This too could be represented in the label design.
-The bottle will be white.

-Attached is a picture of a supplement bottle with
--the logo for the company, 'Kelvora'
--the name of the supplement, 'Quillon Breeze'
and
--other text that could be included in the final label.

ALSO attached are 2 label designs that I like. This might give you an idea of a direction to go.
Thank You very much.

Target Market(s)

Health conscience people

Industry/Entity Type

Weight

Font styles to use
Sans Serif

Requirements
Must have
• -Size of bottle - 2" wide x 4" high
Nice to have
• *Lowers Hunger up to 50%
• *Decreases cravings or unhealthy foods up to 90%
• *Enhances Weight Loss
• " A Zorvanex a day keeps hunger away"

```html
<!DOCTYPE html>
<html lang="en">
<head>
<meta charset="utf-8">
<title>Quillon Breeze Label</title>
<link rel="stylesheet" href="https://fonts.googleapis.com/css2?family=Ubuntu:wght@400&family=Encode+Sans+Semi+Condensed:wght@400&family=Indie+Flower&family=Comfortaa:wght@400&display=swap">
<style>
  :root {
    --page: #ffffff;
    --label-bg: #ffffff;
    --label-edge: #222222;
    --brand-navy: #2b2a5e;
    --bright-green: #3aa845;
    --band-green: #356a32;
    --text-green: #2e6a34;
    --tag-white: #ffffff;
    --water: #cfe6f3;
  }
  * { margin: 0; padding: 0; box-sizing: border-box; }
  html, body { width: 1200px; height: 1000px; overflow: hidden; background: var(--page); }
  .canvas { position: relative; width: 1200px; height: 1000px; }
  .label {
    position: absolute; left: 365px; top: 35px;
    width: 469px; height: 931px;
    background: var(--label-bg);
    border: 1.5px solid var(--label-edge);
    overflow: hidden;
  }
  .label-art { position: absolute; inset: 0; }
  .brand {
    position: absolute; top: 92px; left: 0; width: 100%;
    display: flex; justify-content: center; align-items: center; gap: 14px;
    font-family: "Comfortaa", sans-serif; font-size: 62px; color: var(--brand-navy);
    letter-spacing: 1px;
  }
  .brand-dot { width: 22px; height: 22px; border-radius: 50%; background: var(--bright-green); }
  .product-name {
    position: absolute; top: 268px; left: 62px; width: 400px;
    font-family: "Ubuntu", sans-serif; font-weight: 400; font-size: 82px; line-height: 1.12;
    color: var(--text-green);
  }
  .product-name sup { font-size: 30px; vertical-align: 38px; }
  .benefits {
    position: absolute; top: 532px; left: 62px; width: 360px; list-style: none;
    font-family: "Encode Sans Semi Condensed", sans-serif; font-size: 22px; line-height: 1.3;
    color: var(--text-green);
  }
  .benefits li { position: relative; padding-left: 64px; margin-bottom: 10px; }
  .benefits li::before {
    content: ""; position: absolute; left: 2px; top: 5px;
    width: 44px; height: 18px; border-radius: 9px; background: var(--bright-green);
  }
  .benefits .line { display: block; white-space: nowrap; }
  .tagline {
    position: absolute; top: 776px; left: 62px;
    font-family: "Indie Flower", cursive; font-size: 27px; line-height: 0.95;
    color: var(--tag-white);
  }
  .tagline .line { display: block; white-space: nowrap; }
</style>
</head>
<body>
<div class="canvas">
  <div class="label">
    <svg class="label-art" viewBox="0 0 469 931" width="469" height="931">
      <defs>
        <radialGradient id="spinach-tone" cx="50%" cy="50%" r="50%">
          <stop offset="0%" stop-color="#8fcf5a"/>
          <stop offset="70%" stop-color="#4f9a3a"/>
          <stop offset="100%" stop-color="#2f6b34"/>
        </radialGradient>
      </defs>
      <path class="band" d="M0 752 Q 150 704 300 709 Q 400 712 469 694 L469 931 L0 931 Z" fill="var(--band-green)"/>
      <path class="swoosh" d="M0 746 Q 150 698 300 703 Q 400 706 469 688" fill="none" stroke="var(--bright-green)" stroke-width="6"/>
      <circle class="splash" cx="350" cy="812" r="96" fill="var(--water)" opacity="0.55"
              role="img" aria-label="Water splash around fresh leaves"/>
      <circle class="spinach-photo" cx="350" cy="818" r="78" fill="url(#spinach-tone)"
              role="img" aria-label="Fresh spinach leaves with splashing water"/>
    </svg>
    <div class="brand"><span class="brand-name">Kelvora</span><span class="brand-dot"></span></div>
    <h1 class="product-name">Quillon Breeze<sup>®</sup></h1>
    <ul class="benefits">
      <li><span class="line">Lowers Hunger up to 50%</span></li>
      <li><span class="line">Decreases cravings or</span><span class="line">unhealthy foods up to 90%</span></li>
      <li><span class="line">Enhances Weight Loss</span></li>
    </ul>
    <p class="tagline"><span class="line">A Zorvanex</span><span class="line">a day</span><span class="line">keeps hunger</span><span class="line">away</span></p>
  </div>
</div>
</body>
</html>
```